Business Card Design

We are an IT staffing and consulting company providing IT solutions and resources to our clients.

Industry/Entity Type

Business

Contact Information for Business Card

Ramesh Tulavarthi
Vice President

BrightNode Inc
48215 Harrowmere Court Square, suite 700
Fairbrook, VA 20990
Direct: 571-555-0193
Mobile: 571-555-0147
Email: Ramesh@brightnodeinc.com
Fax: 703-555-0162
www.brightnodeinc.com

```html
<!DOCTYPE html>
<html lang="en">
<head>
<meta charset="utf-8">
<title>BrightNode Inc — Business Card</title>
<link href="https://fonts.googleapis.com/css2?family=Source+Sans+3:wght@300;400;600&display=swap" rel="stylesheet">
<style>
  :root {
    --bg: #e9e6e1;
    --red: #b5162a;
    --red-dark: #8f0f20;
    --white: #ffffff;
    --ink: #3a3a3a;
    --grey-bar: #3b3b3d;
    --black: #0b0b0c;
    --black-soft: #1c1c1e;
  }
  * { margin: 0; padding: 0; box-sizing: border-box; }
  html, body { width: 1200px; height: 902px; overflow: hidden; }
  body {
    background: var(--bg);
    font-family: "Source Sans 3", "Myriad Pro", sans-serif;
    position: relative;
  }
  .card {
    position: absolute;
    left: 280px;
    width: 640px;
    height: 366px;
    border-radius: 22px;
    overflow: hidden;
    box-shadow: 0 10px 26px rgba(0,0,0,.22);
  }
  /* Back */
  .card-back {
    top: 40px;
    background: radial-gradient(ellipse at 40% 35%, var(--black-soft), var(--black) 70%);
    display: flex;
    align-items: center;
    justify-content: center;
  }
  .wordmark {
    font-weight: 300;
    color: var(--red);
    letter-spacing: 1px;
    display: flex;
    align-items: center;
    gap: 10px;
    white-space: nowrap;
  }
  .wordmark .mark-dot {
    width: 12px; height: 12px; background: var(--red); flex: none;
  }
  .card-back .wordmark { font-size: 46px; }

  /* Front */
  .card-front {
    top: 496px;
    background: var(--white);
  }
  .front-logo {
    position: absolute;
    left: 0; top: 0;
    width: 280px; height: 100%;
    display: flex; align-items: center; justify-content: center;
  }
  .front-logo .wordmark { font-size: 36px; }
  .info-panel {
    position: absolute;
    left: 280px; top: 0;
    width: 360px; height: 100%;
    background: linear-gradient(180deg, var(--red), var(--red-dark));
  }
  .name-band {
    position: absolute;
    left: 0; top: 34px;
    width: 100%; height: 66px;
    background: var(--white);
    padding: 10px 20px 0 62px;
  }
  .name-band::after {
    content: "";
    position: absolute;
    left: 0; bottom: -9px;
    width: 100%; height: 9px;
    background: var(--grey-bar);
  }
  .person-name {
    font-size: 21px;
    font-weight: 400;
    color: var(--ink);
    letter-spacing: .5px;
    text-transform: uppercase;
    white-space: nowrap;
  }
  .person-name .first { color: var(--red); }
  .person-title { font-size: 15px; color: var(--ink); margin-top: 2px; }
  .icon-rail {
    position: absolute;
    left: 0; top: 100px;
    width: 40px; height: 266px;
    background: var(--grey-bar);
  }
  .contact-list {
    position: absolute;
    left: 0; top: 122px;
    width: 100%;
    list-style: none;
  }
  .contact-list li {
    display: flex;
    align-items: flex-start;
    color: var(--white);
    font-size: 14.5px;
    line-height: 19px;
    margin-bottom: 9px;
  }
  .contact-list .icon {
    width: 40px; flex: none;
    display: flex; justify-content: center; padding-top: 2px;
  }
  .contact-list .icon svg { width: 14px; height: 14px; fill: var(--white); }
  .contact-list .text { padding-left: 20px; white-space: nowrap; }
</style>
</head>
<body>

<section class="card card-back" aria-label="Card back">
  <div class="wordmark"><span class="mark-dot"></span><span>BrightNode</span></div>
</section>

<section class="card card-front" aria-label="Card front">
  <div class="front-logo">
    <div class="wordmark"><span class="mark-dot"></span><span>BrightNode</span></div>
  </div>
  <div class="info-panel">
    <div class="name-band">
      <div class="person-name"><span class="first">Ramesh</span> Tulavarthi</div>
      <div class="person-title">Vice President</div>
    </div>
    <div class="icon-rail"></div>
    <ul class="contact-list">
      <li>
        <span class="icon"><svg viewBox="0 0 24 24"><path d="M12 2a7 7 0 0 0-7 7c0 5 7 13 7 13s7-8 7-13a7 7 0 0 0-7-7zm0 9.5A2.5 2.5 0 1 1 12 6.5a2.5 2.5 0 0 1 0 5z"/></svg></span>
        <span class="text">48215 Harrowmere Court Square,<br>suite 700 Fairbrook, VA 20990</span>
      </li>
      <li>
        <span class="icon"><svg viewBox="0 0 24 24"><path d="M6.6 10.8a15 15 0 0 0 6.6 6.6l2.2-2.2a1 1 0 0 1 1-.25 11.4 11.4 0 0 0 3.6.57 1 1 0 0 1 1 1V20a1 1 0 0 1-1 1A17 17 0 0 1 3 4a1 1 0 0 1 1-1h3.5a1 1 0 0 1 1 1c0 1.25.2 2.450.57 3.57a1 1 0 0 1-.25 1z"/></svg></span>
        <span class="text">571-555-0193</span>
      </li>
      <li>
        <span class="icon"><svg viewBox="0 0 24 24"><path d="M7 1h10a2 2 0 0 1 2 2v18a2 2 0 0 1-2 2H7a2 2 0 0 1-2-2V3a2 2 0 0 1 2-2zm0 3v14h10V4z"/></svg></span>
        <span class="text">571-555-0147</span>
      </li>
      <li>
        <span class="icon"><svg viewBox="0 0 24 24"><path d="M6 2h10v5H6zM3 8h18v9h-3v5H6v-5H3zm5 7v5h8v-5z"/></svg></span>
        <span class="text">703-555-0162</span>
      </li>
      <li>
        <span class="icon"><svg viewBox="0 0 24 24"><path d="M2 5h20v14H2zm2 2v.5l8 5 8-5V7zm0 2.8V17h16V9.8l-8 5z"/></svg></span>
        <span class="text">Ramesh@brightnodeinc.com</span>
      </li>
      <li>
        <span class="icon"><svg viewBox="0 0 24 24"><path d="M12 2a10 10 0 1 0 0 20 10 10 0 0 0 0-20zm-1 2.1V11H4.1A8 8 0 0 1 11 4.1zm2 0A8 8 0 0 1 19.9 11H13zM4.1 13H11v6.9A8 8 0 0 1 4.1 13zM13 19.9V13h6.9A8 8 0 0 1 13 19.9z"/></svg></span>
        <span class="text">www.brightnodeinc.com</span>
      </li>
    </ul>
  </div>
</section>

</body>
</html>
```